3 glossy INFOGRAPHIC SPLASH PAGES for website of video production / photography studio website

Hello. We need 3 designed infographic images to act as 'splash pages' on our work-in-progress website to offer detailed information to visitors.
1. MUDMAP
2. RATECARD
3. STUDIO FLOORPLAN

To view the website WIP - Go here: http://www.pindlevault.com.au/brellak/

Regarding FILE SIZES:

The MUDMAP should sit in landscape with dimensions 2048px wide x 1536px high.

The RATECARD and STUDIO FLOORPLAN should be laid out in PORTRAIT with dimensions 1526px wide x 2048px high.

Regarding DESIGNS:

First is a 'MUD MAP' that details travel and parking directions for visitors to our studio,

Second is a floorplan of our studio space, and

Third is a Studio Hire Rate Card.

We want these images to utilise our new theme / branding / logos (attached) and ultimately these designs need to be easily read and understood.

Attached Files (may not be in order in brief, but here is my list):
FILE 1 - (2- Brellak Studios Floorplan Rough Thursday, 10 December 2015 03:49:32) is a rough sketch of the floorplan with pertinent details.

FILE 2 - (1-brellak_mudmap_sketch Thursday, 10 December 2015 03:49:33A) rough sketch of the MUDMAP we wish to create

FILE 3 - (Federation_Starfleet_Hull_23rd Thursday, 10 December 2015 03:49:33) is the font we have used on our website (and are happy to utilise in these designs too)

FILE 4 - ( 3-BrellakRateCard Thursday, 10 December 2015 03:49:33) contains the details required for the ratecard.

FILE 5 - ( StockBucket - B52-Shadow Thursday, 10 December 2015 03:49:33) This the font used in our logo - please use it too if you see fit.

FILE 6 - (brellak_gold_logo_stacked_1080 Thursday, 10 December 2015 03:49:33) - our logo stack over two lines - please use this in the three documents (or the one line) as you see fit.

FILE 7 - (Brellak_logo_for_web_row Thursday, 10 December 2015 03:49:33) Is the logo over one line (non-stacked). Again, please utilise this or the stacked logo in each document to act as branding.

FILE 8 - ( Brellak_logo_W Thursday, 10 December 2015 03:49:33) - This is purely the 'W' - please use this to identify brellak studios in the mudmap, and could also be placed in the centre of the studios floorplan.

FILE 9 - ( Brellak Website_WIP Thursday, 10 December 2015 03:49:34) This is a layout of our website as a WIP - Will give you an idea of the look and feel of the website thus far.

FILE 10 (YELLOW_GOLD_debc36 Thursday, 10 December 2015 03:49:34) - This is the gold colour we wish to use in type (for headings) - The RBG Value is: #debc36. This is NOT A prerequisite but if you choose to use gold in type or borders etc, then this the gold we wish to use.

FILE 11 - (brellak_website_mood_theme Thursday, 10 December 2015 03:49:34_) - These are the colours and moods employed on our website. Please utilise this theme as a style guide for your designs.

FILE 12 - (12: brellak_googlemaps_for_reference Thursday, 10 December 2015 04:00:03) This is a snapshot of the the google-map of the area and a guide to the MUDMAP we wish to create, although we only need the details provided in the sketch (SEE FILE 2 for MUDMAP SKETCH).

FILE 13 - (studio_floorplan_example Thursday, 10 December 2015 05:06:02) &

FILE 14 - (studio_floorplan_ex2 Thursday, 10 December 2015 05:06:03) are examples of studio floorplans and are a guide to the floorplan we also wish to create - We wish to also add our branding to this (See files 6 + 7) and a big golden W (see FILE 8) in the middle.

Target Market(s)

potential studio hire customers (mainly producers)

Industry/Entity Type

Film Production

Font styles to use
Sans Serif
Other font styles liked:
• I have supplied branding fonts to be used as you see fit.

Colors
fbed22
00a990
0292cd
fece3e
f78f20
f37122

Requirements
Must have
• Supplied logos and branding theme / colours (see attached).
• Predominantly gold colour (specific gold supplied) as well as utilising colour theme (see attached)
Nice to have
• Would be nice if all three images have a continuity in their layout / design

```html
<!DOCTYPE html>
<html lang="en">
<head>
<meta charset="utf-8">
<title>Brellak Studios – Rate Card</title>
<link href="https://fonts.googleapis.com/css2?family=Black+Ops+One&family=Source+Sans+3:wght@400;600;700&display=swap" rel="stylesheet">
<style>
  :root{
    --purple:#6a45a0;
    --lavender:#9d84c9;
    --magenta:#a8479a;
    --gold:#debc36;
    --gold-text:#d4ae45;
    --ink:#2a1f33;
    --panel:#e8e8ea;
  }
  *{margin:0;padding:0;box-sizing:border-box}
  html,body{width:894px;height:1200px;overflow:hidden;background:var(--purple)}
  body{font-family:"Source Sans 3",sans-serif;color:var(--ink);position:relative}
  .abs{position:absolute}
  .frame{left:0;top:0}
  .brand{left:0;width:894px;top:58px;text-align:center;font-family:"Black Ops One",sans-serif;font-size:62px;letter-spacing:4px;color:var(--gold);line-height:1;white-space:nowrap}
  .brand-bar{top:86px;width:30px;height:9px;background:var(--gold)}
  .section-title{font-family:"Black Ops One",sans-serif;font-size:23px;letter-spacing:2px;color:var(--ink);line-height:1;white-space:nowrap}
  .note-gold{color:var(--gold-text);font-weight:700;font-size:13px}
  .panel{background:var(--panel);border-radius:3px}
  .panel-head{color:var(--gold-text);font-weight:700;font-size:22px;text-align:center}
  .rate-grid{display:grid;grid-template-columns:104px 1fr;row-gap:12px;column-gap:14px;padding:0 16px;margin-top:10px;font-weight:700;font-size:16px;line-height:1.2}
  .rate-grid .price{text-align:center}
  .rate-grid .term{padding-top:2px}
  .bump{left:67px;top:213px;width:156px;height:231px;padding-top:18px;text-align:center;font-weight:700;font-size:16px;line-height:1.3}
  .bump p{margin-top:16px}
  .bump p+p{margin-top:26px}
  .weekday{left:259px;top:213px;width:262px;height:231px;padding-top:24px}
  .saturday{left:558px;top:213px;width:262px;height:231px;padding-top:24px}
  .footnote{right:76px;top:456px;font-weight:700;font-size:13px;color:var(--ink)}
  .dedicated-frame{left:72px;top:505px;width:296px;height:67px;border:9px dashed var(--gold-text);display:flex;align-items:center;justify-content:center}
  .dedicated-frame .section-title{font-size:20px;letter-spacing:1px}
  .dedicated-rates{left:375px;top:496px;width:242px;height:92px;padding:10px 18px;display:grid;grid-template-columns:1fr auto;row-gap:8px;align-items:center}
  .dedicated-rates .day{color:var(--gold-text);font-weight:700;font-size:22px}
  .dedicated-rates .amt{font-weight:700;font-size:15px}
  .dedicated-desc{left:71px;top:597px;width:560px;font-size:12px;line-height:1.3}
  .dedicated-desc small{display:block;color:var(--ink);font-weight:700;font-size:11.5px;margin-top:4px}
  .extras{left:642px;top:486px;width:210px;font-size:12px;font-weight:700;line-height:1.3}
  .extras .section-title{font-size:21px;margin-left:55px;margin-bottom:10px}
  .extras .label,.equipment .label,.terms .label{color:var(--gold-text)}
  .equipment{left:642px;top:716px;width:210px;font-size:12px;font-weight:700;line-height:1.3}
  .hours{left:69px;top:700px;width:342px;height:131px;padding:10px 10px;font-weight:700}
  .hours .lead{font-size:13.5px}
  .hours-row{display:grid;grid-template-columns:130px 1fr;align-items:center;margin-top:4px;padding-left:8px}
  .hours-row .day{color:var(--gold-text);font-size:22px}
  .hours-row .time{font-size:16px}
  .hours .foot{font-size:13px;margin-top:6px}
  .terms{left:67px;top:903px;width:615px;font-size:11.3px;font-weight:700;line-height:1.3}
  .terms p{margin-bottom:11px}
  .art{position:absolute}
</style>
</head>
<body>

<svg class="abs frame" width="894" height="1200" viewBox="0 0 894 1200" aria-hidden="true">
  <rect x="38" y="38" width="818" height="1124" rx="30" fill="none" stroke="var(--lavender)" stroke-width="11" stroke-dasharray="13 13"/>
</svg>

<div class="art" role="img" aria-label="Illustration of a studio spotlight" style="left:657px;top:88px;width:183px;height:118px;border-radius:40px;background:linear-gradient(135deg,#b49ad9,#8d72c0);opacity:.8"></div>

<span class="abs brand-bar" style="left:64px"></span>
<h1 class="abs brand">BRELLAK STUDIOS</h1>
<span class="abs brand-bar" style="left:800px"></span>

<h2 class="abs section-title" style="left:92px;top:146px">SOUND PROOF STUDIO HIRE</h2>
<p class="abs note-gold" style="left:67px;top:184px">Video Studio Hire includes:10 &amp; 15 amp power outlets, NBN Enabled ethernet &amp; wi-fi, toilet.</p>

<section class="abs panel bump">
  <div class="panel-head">Bump In/Out</div>
  <p>$180<br>p/4hrs</p>
  <p>Available<br>weekdays only</p>
</section>

<section class="abs panel weekday">
  <div class="panel-head">Mon-Fri</div>
  <div class="rate-grid">
    <span class="price">$350<br>p/half day</span><span class="term">Up to 5 hours*</span>
    <span class="price">$550<br>p/half day</span><span class="term">Up to 10 hours</span>
    <span class="price">$150 p/hr<br>overtime</span><span class="term">Beyond 10<br>hours</span>
  </div>
</section>

<section class="abs panel saturday">
  <div class="panel-head">Saturday</div>
  <div class="rate-grid">
    <span class="price">$450<br>p/half day</span><span class="term">Up to 5 hours*</span>
    <span class="price">$650<br>p/half day</span><span class="term">Up to 10 hours</span>
    <span class="price">$200 p/hr<br>overtime</span><span class="term">Beyond 10<br>hours</span>
  </div>
</section>

<div class="art" role="img" aria-label="Star badge illustration" style="left:67px;top:387px;width:128px;height:128px;border-radius:50%;background:radial-gradient(circle,#c77fb8 0%,#a8479a 55%,#8a6cc0 80%);border:6px solid #8a6cc0"></div>

<p class="abs footnote">*Any half day rental that exceeds 5 hours automatically becomes a full day hire.</p>

<div class="abs dedicated-frame"><h2 class="section-title">DEDICATED CLIENT</h2></div>

<section class="abs panel dedicated-rates">
  <span class="day">Mon-Fri</span><span class="amt">$250 p/day</span>
  <span class="day">Saturday</span><span class="amt">$300 p/day</span>
</section>

<div class="abs dedicated-desc">
  <span class="note-gold" style="font-size:12px">Dedicated Client Viewing Area includes coffee machine, bottled water, fridge, 65” 4k viewing monitor, leather couch, boardroom table, additional bathroom &amp; toilet, NBN enabled ethernet &amp; wifi.</span>
  <small>(To be used in conjunction with studio hire only)</small>
</div>

<aside class="abs extras">
  <h2 class="section-title">EXTRAS</h2>
  <p><span class="label">Catering:</span> Contact us for healthy, fresh, locally sourced catering options. Gluten Free and vegetarian options also available.</p>
</aside>

<div class="art" role="img" aria-label="Clapperboard with catering icons illustration" style="left:648px;top:608px;width:157px;height:96px;border-radius:20px;background:linear-gradient(180deg,#a890d4 0%,#a8479a 60%,#8d72c0 100%)"></div>

<p class="abs equipment"><span class="label">Equipment:</span> Reference monitor, C-Stands and Lighting stands available on request for additional fee.</p>

<div class="art" role="img" aria-label="Lighting and C-stand equipment illustration" style="left:662px;top:774px;width:178px;height:93px;border-radius:14px;background:linear-gradient(180deg,#8f79c2 0%,#b24fa0 100%)"></div>

<h2 class="abs section-title" style="left:92px;top:666px">OPENING HOURS</h2>

<div class="art" role="img" aria-label="Video camera illustration" style="left:420px;top:630px;width:200px;height:215px;border-radius:60px;background:linear-gradient(135deg,#b9a3dc 0%,#a8479a 55%,#8a6cc0 100%)"></div>

<section class="abs panel hours">
  <p class="lead">For advanced Studio bookings.</p>
  <div class="hours-row"><span class="day">Weekdays</span><span class="time">7 am</span></div>
  <div class="hours-row"><span class="day">Weekends</span><span class="time">9 am</span></div>
  <p class="foot">Earlier opening times can be arranged on request.</p>
</section>

<h2 class="abs section-title" style="left:92px;top:864px">TERMS AND CONDITIONS</h2>

<div class="art" role="img" aria-label="Director's chair illustration" style="left:692px;top:960px;width:130px;height:190px;border-radius:24px;background:linear-gradient(180deg,#9a82c8 0%,#a8479a 55%,#8d72c0 100%)"></div>

<div class="abs terms">
  <p><span class="label">Payment:</span> 14 day account terms applies to all verified account holders, otherwise payment must be made in full at end of usage (via eftpos).</p>
  <p><span class="label">Cancellation:</span> Cancellation fees apply to bookings cancelled less than 24 hours before agreed studio hire start time.</p>
  <p><span class="label">Damage Policy:</span> Brellak Studios understands that sometimes things happen, and general wearandtear is an unavoidable fact of life. However, if significant damage or breakages occur, the cost of repair or replacement will be placed solely onto the Hirer. We also expect our studio wall to be left in the same relative condition as it was found, and any significant damage will result in a replastering and repainting fee of $350.</p>
  <p>At Brellak Studios, we endeavour to make your shooting experience run as smoothly as possible. We are here to listen to your requirements and assist you in any way, so feel free to contact us well before your shoot to see how we can help.</p>
  <p>Brellak Studios is also equipped with 24 hour CCTV and is fully alarmed.</p>
  <p>Unless otherwise indicated, all prices above are exclusive of GST.</p>
</div>

</body>
</html>
```